Postcard Design

I am a speech pathologist. My company is called Kite Parade. I have a program called "Bright Knots" to help children stop sucking their thumb/ fingers. After they complete the program, I need to check in after 6 months to make sure they have continued with their success, and to see if they may be ready for the follow up program "Lark Steps" for those with a tongue thrust.

On one side, I would like "Kite Parade....Bright Knots to your success!" with my logo. On the other side, I would like a reflective sticker like a mirror that says something like "Kite parade...it's time to check your smile". Please contact Marisol if you think a Tongue thrust may be present. Lark Steps is a follow up program to retrain the tongue to work properly in the mouth. Please discuss with your orthodontist/ dentist or contact Marisol if you want to schedule an evaluation.
Updates

Reason: Just trying to make sure I get the best postcard as possible. I've extended the deadline by a few days to see what else comes in and to tweak the changes I've already received. Thanks!

Target Market(s)

families and children

Industry/Entity Type

It Company

Requirements
Must have
• logos for Kite Parade, Bright Knots, and Lark Steps
Nice to have
• I had this idea of a paper reflective mirror for the back so the children can actually see their smile when they look in it, but know that may be impossible. Just a creative idea.

```html
<!DOCTYPE html>
<html lang="en">
<head>
<meta charset="utf-8">
<title>Kite Parade Postcard</title>
<link rel="stylesheet" href="https://fonts.googleapis.com/css2?family=Indie+Flower&display=swap">
<style>
  :root {
    --page: #ffffff;
    --pink: #e08fbd;
    --pink-soft: #eaaed0;
    --white: #ffffff;
    --ink: #1c1c1c;
    --card-edge: #cfcfcf;
    --art-grey: #e6e6e6;
  }
  * { margin: 0; padding: 0; box-sizing: border-box; }
  html, body {
    width: 927px; height: 1200px; overflow: hidden;
    background: var(--page);
    font-family: "Indie Flower", cursive;
  }
  .canvas { position: relative; width: 927px; height: 1200px; }

  .postcard-front {
    position: absolute; left: 173px; top: 111px;
    width: 544px; height: 381px;
    background: var(--pink);
    overflow: hidden;
  }
  .swirl-backdrop {
    position: absolute; inset: 0;
    background:
      radial-gradient(circle at 12% 80%, var(--pink-soft) 0, transparent 22%),
      radial-gradient(circle at 20% 30%, var(--pink-soft) 0, transparent 12%),
      radial-gradient(circle at 70% 88%, var(--pink-soft) 0, transparent 16%),
      radial-gradient(circle at 92% 72%, var(--pink-soft) 0, transparent 12%);
    opacity: 0.7;
  }
  .logo-mark {
    position: absolute; left: 143px; top: 58px;
    width: 267px; height: 147px;
    background: var(--pink-soft);
    border-radius: 20px;
  }
  .brand-name {
    position: absolute; left: 0; right: 0; top: 214px;
    text-align: center;
    color: var(--white);
    font-size: 66px; font-weight: 400; line-height: 1;
  }
  .tagline {
    position: absolute; right: 23px; top: 305px;
    color: var(--white);
    font-size: 18px; line-height: 1;
  }

  .postcard-back {
    position: absolute; left: 173px; top: 531px;
    width: 544px; height: 380px;
    background: var(--white);
    border: 1px solid var(--card-edge);
  }
  .message {
    position: absolute; left: 18px; top: 4px; width: 350px;
    color: var(--ink);
    font-size: 13.5px; line-height: 24px;
    text-align: justify;
  }
  .divider {
    position: absolute; left: 372px; top: 14px;
    width: 2px; height: 349px;
    background: var(--ink);
  }
  .stamp-box {
    position: absolute; left: 451px; top: 19px;
    width: 77px; height: 90px;
    border: 1.5px solid var(--ink);
    display: flex; align-items: flex-start; justify-content: center;
    padding-top: 26px;
    font-size: 17px; color: var(--ink);
  }
  .smile-art {
    position: absolute; left: 18px; top: 262px;
    width: 98px; height: 98px;
    border-radius: 50%;
    background: var(--art-grey);
  }
  .speech-bubble {
    position: absolute; left: 100px; top: 238px;
    width: 84px; height: 46px;
  }
  .speech-bubble span {
    position: absolute; left: 10px; top: 4px; width: 74px;
    text-align: center;
    font-size: 15px; color: var(--ink);
  }
</style>
</head>
<body>
<main class="canvas">
  <section class="postcard-front">
    <div class="swirl-backdrop" role="img" aria-label="Soft pale pink swirl pattern in the background"></div>
    <div class="logo-mark" role="img" aria-label="Kite Parade illustration area"></div>
    <h1 class="brand-name">Kite Parade</h1>
    <p class="tagline">Bright knots to your success!</p>
  </section>

  <section class="postcard-back">
    <p class="message">"Kite parade...it's time to check your smile". Please contact Marisol if you think a Tongue thrust may be present. Lark Steps is a follow up program to retrain the tongue to work properly in the mouth. Please discuss with your orthodontist/ dentist or contact Marisol if you want to schedule an evaluation..</p>
    <div class="divider"></div>
    <div class="stamp-box">Stamp</div>
    <div class="smile-art" role="img" aria-label="Sketched smiling character showing teeth"></div>
    <div class="speech-bubble">
      <svg width="84" height="46" viewBox="0 0 84 46" aria-hidden="true">
        <path d="M18 4 H76 a6 6 0 0 1 6 6 V26 a6 6 0 0 1 -6 6 H26 L6 44 L16 30 a6 6 0 0 1 -6 -4 V10 a6 6 0 0 1 6 -6 Z"
              fill="none" stroke="#1c1c1c" stroke-width="1"/>
      </svg>
      <span>Smile !!!</span>
    </div>
  </section>
</main>
</body>
</html>
```